Business Card & Letterhead Design

We a financial advice company based in Australia. We provide advice to wealthy farmers.

We are changing our business name FROM Brightmere Financial TO Calderstone Wealth and we need a new letterhead and double sided business card design

Attached is designs from our previous branding (Brightmere Financial) as it includes all the details we require on the new Calderstone Wealth business cards and letterhead.

```html
<!DOCTYPE html>
<html lang="en">
<head>
<meta charset="utf-8">
<title>Calderstone Wealth Letterhead</title>
<link href="https://fonts.googleapis.com/css2?family=Arimo:wght@400;700&display=swap" rel="stylesheet">
<style>
  :root {
    --backdrop: #7fd6f2;
    --paper: #f2f3f4;
    --paper-shade: #e8eaec;
    --ink: #2c2f34;
    --ink-soft: #55595f;
    --band: #2b2e33;
    --accent: #2bb4d6;
    --mark-faint: #d9dde1;
    --white: #ffffff;
  }
  * { margin: 0; padding: 0; box-sizing: border-box; }
  html, body {
    width: 1200px; height: 899px; overflow: hidden;
    background: var(--backdrop);
    font-family: "Arimo", Arial, sans-serif;
  }
  .letterhead {
    position: absolute; left: 300px; top: 20px;
    width: 600px; height: 860px;
    background: linear-gradient(180deg, var(--paper) 0%, var(--paper-shade) 100%);
    overflow: hidden;
  }
  .brand {
    position: absolute; right: 42px; top: 58px;
    text-align: right;
  }
  .brand-dot {
    display: block; width: 36px; height: 36px;
    border: 1.5px solid var(--ink); border-radius: 50%;
    margin: 0 36px 8px auto;
  }
  .brand-name {
    font-size: 13px; font-weight: 400; letter-spacing: 0.6px;
    color: var(--ink); text-transform: uppercase;
  }
  .brand-sub {
    font-size: 5px; letter-spacing: 2.4px; color: var(--ink-soft);
    text-transform: uppercase; margin-top: 2px;
  }
  .details {
    position: absolute; right: 42px; top: 132px;
    text-align: right; font-size: 8.6px; line-height: 11px;
    color: var(--ink-soft); letter-spacing: 0.4px;
  }
  .details .entity { font-weight: 700; color: var(--ink); font-size: 9.2px; }
  .details .group { margin-bottom: 6px; }
  .details .label { color: var(--accent); }
  .details .web { color: var(--accent); }
  .watermark {
    position: absolute; left: 129px; top: 346px;
    width: 336px; height: 336px;
  }
  .footer-band {
    position: absolute; left: 15px; right: 15px; top: 742px; bottom: 0;
    background: var(--band);
    border-radius: 30px 30px 0 0;
  }
  .footer-mark {
    position: absolute; left: 17px; top: 15px;
    display: flex; align-items: center; gap: 6px;
    color: var(--white); font-size: 8px; font-weight: 700; letter-spacing: 0.3px;
  }
  .footer-dot {
    width: 26px; height: 26px; border: 1.5px solid var(--white); border-radius: 50%;
  }
  .footer-legal {
    position: absolute; right: 34px; top: 10px;
    text-align: right; color: var(--white);
    font-size: 6.6px; line-height: 7.6px; letter-spacing: 0.6px;
  }
  .address-tab {
    position: absolute; left: 207px; top: 780px;
    width: 183px; height: 100px;
    background: var(--paper-shade);
    border-radius: 12px 12px 0 0;
    text-align: center;
  }
  .tagline {
    margin-top: 3px; font-size: 8.6px; letter-spacing: 0.8px;
    color: var(--accent);
  }
</style>
</head>
<body>
  <main class="letterhead">
    <header class="brand">
      <span class="brand-dot"></span>
      <div class="brand-name">Calderstone Wealth</div>
      <div class="brand-sub">Strategic Financial Advice</div>
    </header>

    <section class="details">
      <div class="group">
        <div class="entity">Tallowood Holdings Pty Ltd</div>
        <div class="entity">ATF The Marlow Investment</div>
        <div class="entity">Trust T/AS Brightmere Financial</div>
        <div>ABN: 00 111 222 333</div>
        <div>Corporate Authorised</div>
        <div>Representative of Harbourline</div>
        <div>Advisory Limited</div>
      </div>
      <div class="group">
        <div>Suite 4A, 18 Wattle St</div>
        <div>Riverbend QLD 4101</div>
        <div>PO Box 5210</div>
        <div>Riverbend QLD 4101</div>
        <div><span class="label">p</span> (07) 3000 1234</div>
        <div><span class="label">f</span> (07) 3000 5678</div>
      </div>
      <div>admin@<span class="web">brightmerefinancial</span>.example</div>
      <div>www.<span class="web">brightmerefinancial</span>.example</div>
    </section>

    <svg class="watermark" viewBox="0 0 336 336" aria-hidden="true">
      <circle cx="168" cy="168" r="164" fill="none" stroke="var(--mark-faint)" stroke-width="5"/>
    </svg>

    <footer class="footer-band">
      <div class="footer-mark">
        <span class="footer-dot"></span>
        <span>A referral built business</span>
      </div>
      <div class="footer-legal">
        <div>Harbourline Advisory Limited</div>
        <div>ABN 00 444 555 666</div>
        <div>Australian Financial Services Licence</div>
        <div>Licence Number 000 123</div>
        <div>Principal Address: 410 Harbour Rd</div>
        <div>PO Box 1000 Melbourne VIC 3000</div>
      </div>
    </footer>
    <div class="address-tab">
      <p class="tagline">'financial peace of mind'</p>
    </div>
  </main>
</body>
</html>
```